I am a Financial Adviser specialising in Aged Care Advice. We provide financial advice and assistance to families with loved ones entering an Aged Care facility.
We need a flyer detailing the Aged Care Packages that we offer. There will be 3 main packages & then other add ons. I need an area where the client can sign off on the package/s that they choose. I have attached a sample to demonstrate the required layout, and a copy of content. I would like the flyer to have an image as per the attached sample, and to be designed in soft pastels, blues, greens.

Financial

```html
<!DOCTYPE html>
<html lang="en">
<head>
<meta charset="utf-8">
<title>Evergreen Advisory – Aged Care Services</title>
<link href="https://fonts.googleapis.com/css2?family=Open+Sans:ital,wght@0,300;0,400;0,600;0,700;1,300;1,400&family=Tangerine:wght@400;700&display=swap" rel="stylesheet">
<style>
  :root{
    --backdrop:#d6d7d9;
    --sage:#dcdbb0;
    --sage-deep:#a9b26a;
    --brown:#9b7651;
    --brown-dark:#7d5c3d;
    --gold:#b07d3a;
    --ink:#3b3b3b;
    --ink-soft:#5a5a5a;
    --paper:#ffffff;
    --rule:#a78a67;
  }
  *{box-sizing:border-box;margin:0;padding:0}
  html,body{width:1200px;height:900px;overflow:hidden;background:var(--backdrop);font-family:"Open Sans",Arial,sans-serif;color:var(--ink)}
  .canvas{position:relative;width:1200px;height:900px}
  .page{position:absolute;top:53px;width:562px;height:795px;background:var(--paper);overflow:hidden;box-shadow:0 2px 6px rgba(0,0,0,.25)}
  .page--front{left:24px}
  .page--back{left:625px}

  /* front page */
  .front-header{position:absolute;left:0;top:0;width:562px;height:325px;background:var(--sage)}
  .hero-photo{position:absolute;left:0;top:0;width:341px;height:272px;border-bottom-right-radius:44px;
    background:radial-gradient(ellipse at 55% 45%,#e9c9b4 0%,#d9ab92 35%,#b9a787 65%,#cfd3a4 100%);
    box-shadow:6px 4px 0 var(--sage-deep)}
  .brand{position:absolute;left:378px;top:108px;display:flex;align-items:center;gap:8px}
  .brand-dot{width:12px;height:12px;border-radius:50%;background:var(--gold)}
  .brand-name{font-size:19px;font-weight:600;color:var(--ink);line-height:1.05}
  .front-sage-strip{position:absolute;left:0;top:272px;width:562px;height:53px;background:var(--sage)}
  .title-band{position:absolute;right:0;top:280px;width:306px;height:45px;background:var(--brown);border-top-left-radius:30px;
    color:#fff;font-style:italic;font-weight:300;font-size:27px;line-height:45px;padding-left:36px;white-space:nowrap}
  .tagline{position:absolute;left:22px;width:220px;text-align:center}
  .tagline-script{font-family:"Tangerine",cursive;font-weight:700;font-size:34px;color:var(--gold);line-height:1}
  .tagline-script .star{font-family:"Open Sans",sans-serif;font-size:12px;color:var(--brown);vertical-align:middle;margin-right:6px}
  .tagline-sub{font-size:13.5px;color:var(--ink-soft);line-height:16px;margin-top:4px}
  .package{position:absolute;left:254px;width:300px}
  .package-head{display:flex;align-items:center;gap:6px;font-weight:700;font-size:13.5px;color:var(--ink)}
  .check{width:16px;height:16px;border:1px solid #777;background:#fff;flex:none}
  .package-base{font-size:10px;font-weight:700;color:var(--ink);margin-top:1px}
  .package-list{list-style:none;margin-top:7px;font-size:10px;line-height:13.6px;color:var(--ink-soft)}
  .package-note{margin-top:10px;font-size:7.6px;line-height:10px;color:var(--ink-soft)}
  .front-footer{position:absolute;left:0;top:765px;width:562px;height:30px;background:var(--brown)}
  .front-footer svg{position:absolute;right:0;top:0}

  /* back page */
  .back-header{position:absolute;left:0;top:0;width:562px;height:492px;background:var(--sage)}
  .options-tab{position:absolute;left:0;top:0;width:222px;height:44px;background:var(--brown);border-bottom-right-radius:30px;
    color:#fff;font-style:italic;font-weight:400;font-size:19px;line-height:48px;padding-left:31px;white-space:nowrap}
  .care-photo{position:absolute;left:310px;top:0;width:252px;height:215px;border-bottom-left-radius:44px;
    background:linear-gradient(135deg,#5f7a45 0%,#8fa06a 35%,#c8c6c4 60%,#7f8fa0 100%);
    box-shadow:-6px 5px 0 var(--sage-deep)}
  .option{position:absolute;left:34px;width:500px}
  .option-head{display:flex;align-items:center;gap:6px;font-weight:700;font-size:11.5px;color:var(--ink)}
  .option-head .check{width:15px;height:15px}
  .option-text{font-size:8.4px;line-height:11.6px;color:var(--ink-soft);margin-top:1px}
  .option--narrow{width:262px}
  .agreement{position:absolute;left:34px;top:508px;width:500px;font-size:11px;line-height:16px;color:var(--ink-soft)}
  .agreement-rule{position:absolute;left:34px;top:588px;width:492px;border-top:1.5px solid var(--rule)}
  .sign{position:absolute;font-size:11px;color:var(--ink-soft)}
  .sign-line{display:block;font-size:9px;letter-spacing:.5px;color:#777;height:12px}
  .back-footer{position:absolute;left:0;top:702px;width:562px;height:93px;background:var(--brown);padding:7px 12px 0 14px;color:#f1e6d6}
  .back-footer-title{font-size:9px;font-style:italic;font-weight:400}
  .back-footer p{font-size:7.4px;line-height:9.2px}
</style>
</head>
<body>
<main class="canvas">

  <section class="page page--front">
    <div class="front-header"></div>
    <div class="hero-photo" role="img" aria-label="Photo of a younger hand gently holding an elderly person's hand"></div>
    <div class="brand"><span class="brand-dot"></span><span class="brand-name">Evergreen<br>Advisory</span></div>
    <div class="front-sage-strip"></div>
    <h1 class="title-band">Aged Care Services</h1>

    <div class="tagline" style="top:368px">
      <div class="tagline-script"><span class="star">★</span>Peace of Mind</div>
      <p class="tagline-sub">...When you know<br>what you want...</p>
    </div>
    <div class="tagline" style="top:520px">
      <div class="tagline-script"><span class="star">★</span>Confidence</div>
      <p class="tagline-sub">....When you need to know<br>all the options....</p>
    </div>
    <div class="tagline" style="top:656px">
      <div class="tagline-script"><span class="star">★</span>Convenience</div>
      <p class="tagline-sub">....When you need someone<br>to take charge....</p>
    </div>

    <div class="package" style="top:354px">
      <div class="package-head"><span class="check"></span>ESSENTIALS Package $770</div>
      <ul class="package-list">
        <li>Explanation of Aged Care Fees and Charges.</li>
        <li>Preliminary Home/Assets Assessment.*</li>
        <li>Estimated Means Tested Fee Calculation.*</li>
        <li>Preliminary Aged Care Costs.*</li>
        <li>Estimated Cash Flow Scenario.*</li>
      </ul>
      <p class="package-note">*Please note this is general factual information only.<br>We do not provide any specific personal information.</p>
    </div>

    <div class="package" style="top:506px">
      <div class="package-head"><span class="check"></span>ADVANTAGE Package $2,970</div>
      <div class="package-base">ESSENTIALS Package plus</div>
      <ul class="package-list">
        <li>Analyse and Strategize Aged Care costs.</li>
        <li>Compare up to 5 Strategy options.</li>
        <li>Minimise Aged Care Costs (where possible).</li>
        <li>Maximise Age Pension Income (where possible).</li>
        <li>Prepare a Full Statement of Advice (SOA).</li>
        <li>Implementation of Aged Care Strategy.</li>
      </ul>
    </div>

    <div class="package" style="top:647px">
      <div class="package-head"><span class="check"></span>PLATINUM Package $5,940</div>
      <div class="package-base">ADVANTAGE Package plus</div>
      <ul class="package-list">
        <li>Liase with the Aged Care Facility.</li>
        <li>CentreLink/DVA Nominee.</li>
        <li>Post Entry Review.</li>
        <li>Post Implementation SOA (if required).</li>
        <li>Annual Review.</li>
      </ul>
    </div>

    <div class="front-footer">
      <svg width="290" height="30" viewBox="0 0 290 30"><path d="M0 30 C40 4 70 0 120 0 L290 0 L290 30 Z" fill="var(--sage)"/></svg>
    </div>
  </section>

  <section class="page page--back">
    <div class="back-header"></div>
    <h2 class="options-tab">Extra Choice Options</h2>
    <div class="care-photo" role="img" aria-label="Photo of a carer sitting with a smiling elderly woman outdoors"></div>

    <div class="option option--narrow" style="top:57px">
      <div class="option-head"><span class="check"></span>CentreLink/DVA Nominee $1,100</div>
      <p class="option-text">Communicate with CentreLink/DVA on behalf of our client/s, and undertake all changes and updates to details, as directed by our client.</p>
    </div>
    <div class="option option--narrow" style="top:127px">
      <div class="option-head"><span class="check"></span>Post Implementation Statement of Advice<br>$1,650</div>
      <p class="option-text">Revise our original Advice Statement for any changes of circumstances including income &amp; asset variations, and provide further advice within the first 12 months of initial advice statement.</p>
    </div>
    <div class="option" style="top:223px">
      <div class="option-head"><span class="check"></span>Annual Review $990</div>
      <p class="option-text">A review of the recommendations made in our original advice document, taking into account any changes to client's circumstances including checking current cash flow is sufficient to meet ongoing aged care costs.</p>
    </div>
    <div class="option" style="top:280px">
      <div class="option-head"><span class="check"></span>Post Entry Review $660</div>
      <p class="option-text">Review financial situation, check facility invoices are accurate, explain the Residential Aged Care Agreement and ensure all recommendations are implemented.</p>
    </div>
    <div class="option" style="top:337px">
      <div class="option-head"><span class="check"></span>Facility Liason $550</div>
      <p class="option-text">Negotiate with the Aged Care Facility regarding Accommodation payments, clarify &amp; explain Residential Care Agreement, and review facility invoices.</p>
    </div>
    <div class="option" style="top:393px">
      <div class="option-head"><span class="check"></span>Family Conferences $660</div>
      <p class="option-text">Facilitate &amp; co-ordinate family meetings to explain the Aged Care legislation and how it fits with the family circumstances.</p>
    </div>
    <div class="option" style="top:450px">
      <div class="option-head"><span class="check"></span>Estate Wrap $660</div>
      <p class="option-text">Assist beneficiaries with correct procedures and paperwork regarding the finalisation of the estate.</p>
    </div>

    <div class="agreement">
      <p>I/We have chosen the Service Package and Options as ticked above.</p>
      <p>I/We understand that by choosing the Essentials Package, that I/We are receiving factual information only, and not financial advice.</p>
      <p>I/We agree to pay the amount of ………………….,&nbsp;&nbsp; within seven days of the date of the invoice received from Evergreen Advisory SA.</p>
    </div>
    <div class="agreement-rule"></div>

    <div class="sign" style="left:36px;top:616px"><span class="sign-line">……………………………………………</span>Signature</div>
    <div class="sign" style="left:188px;top:616px"><span class="sign-line">……………………………………………</span>Signature</div>
    <div class="sign" style="left:332px;top:616px"><span class="sign-line">……………………………………………</span>Signature</div>
    <div class="sign" style="left:464px;top:616px"><span class="sign-line">……../………/………</span>Date</div>
    <div class="sign" style="left:34px;top:662px"><span class="sign-line">…………………………………………….</span>Adviser Signature</div>
    <div class="sign" style="left:194px;top:662px"><span class="sign-line">………/………/………</span>Date</div>

    <footer class="back-footer">
      <div class="back-footer-title">Important Information</div>
      <p>This document has been prepared by Evergreen Advisory SA Pty Ltd ABN 00 123 456 789, an Authorised Representative of Northgate Advice Limited ABN 00 987 654 321 AFSL 000000, a wholly owned, non-guaranteed subsidiary of the Southern Cross Banking Group ABN 00 111 222 333.</p>
      <p>Information in this document is based on current regulatory requirements and laws, as at 20 September, 2016 which may be subject to change. It contains general advice. It does not take into account your individual objectives, financial situation or needs. You should consider talking to a financial adviser before making a financial decision.</p>
    </footer>
  </section>

</main>
</body>
</html>
```